Visitenkarte erstellen für Reiki Praxis

Visitenkarten für Reiki Praxis Doppelseitig

business cards reiki practice double-sided

The background can also be a different color

```html
<!DOCTYPE html>
<html lang="en">
<head>
<meta charset="utf-8">
<title>Stillwater Reiki – Business Cards</title>
<link rel="stylesheet" href="https://fonts.googleapis.com/css2?family=Lato:wght@400;700&display=swap">
<style>
  :root {
    --page-bg: #c6c6c6;
    --card-bg: #14111f;
    --gold: #e0a82e;
    --bronze-light: #f5dcc0;
    --bronze-mid: #c8956a;
    --bronze-dark: #8f5e3e;
    --text-light: #f2f0f4;
  }
  * { margin: 0; padding: 0; box-sizing: border-box; }
  html, body {
    width: 1200px; height: 1200px; overflow: hidden;
    background: var(--page-bg);
    font-family: "Lato", Arial, sans-serif;
  }
  .card {
    position: absolute;
    width: 830px; height: 476px;
    background: var(--card-bg);
    overflow: hidden;
  }
  .card--front { left: 189px; top: 91px; }
  .card--back { left: 186px; top: 639px; }

  .line-art {
    position: absolute;
    background:
      radial-gradient(ellipse at 60% 55%, rgba(200,149,106,0.28) 0%, rgba(200,149,106,0.10) 45%, rgba(20,17,31,0) 75%);
  }
  .card--front .line-art { left: 370px; top: 0; width: 460px; height: 476px; }
  .card--back .line-art { left: 0; top: 0; width: 460px; height: 476px;
    background: radial-gradient(ellipse at 40% 55%, rgba(200,149,106,0.28) 0%, rgba(200,149,106,0.10) 45%, rgba(20,17,31,0) 75%); }

  .brand {
    position: absolute;
    display: flex; flex-direction: column; align-items: center;
  }
  .brand__dot {
    width: 46px; height: 46px; border-radius: 50%;
    border: 2px solid var(--bronze-mid);
    margin-bottom: 18px;
  }
  .brand__name {
    font-weight: 400; font-size: 34px; letter-spacing: 1px;
    color: var(--text-light); white-space: nowrap;
  }
  .card--front .brand { left: 47px; width: 334px; top: 62px; }
  .card--back .brand { left: 460px; width: 340px; top: 340px; }

  .accent-bar {
    position: absolute; left: 0; top: 236px; width: 20px; height: 210px;
    background: linear-gradient(180deg, var(--bronze-light) 0%, var(--bronze-mid) 30%, var(--bronze-light) 50%, var(--bronze-mid) 75%, var(--bronze-light) 100%);
  }
  .person { position: absolute; left: 47px; top: 230px; }
  .person__name { font-weight: 700; font-size: 25px; color: var(--gold); letter-spacing: 0.3px; }
  .person__role { font-size: 19px; color: var(--text-light); margin-top: 4px; }

  .contacts { position: absolute; left: 44px; top: 300px; list-style: none; }
  .contacts li {
    display: flex; align-items: flex-start; gap: 10px;
    font-size: 19.5px; line-height: 29px; color: var(--text-light);
  }
  .contacts li + li { margin-top: 0; }
  .contacts .gap { margin-top: 11px; }
  .contacts svg { width: 20px; height: 20px; flex: none; margin-top: 5px; }
</style>
</head>
<body>

<section class="card card--front">
  <div class="line-art" role="img" aria-label="Flowing bronze line-art drawing of a bird with open hands"></div>

  <div class="brand">
    <span class="brand__dot"></span>
    <span class="brand__name">STILLWATER REIKI</span>
  </div>

  <div class="accent-bar"></div>

  <div class="person">
    <div class="person__name">HANNA BERGER</div>
    <div class="person__role">General Manager</div>
  </div>

  <ul class="contacts">
    <li>
      <svg viewBox="0 0 20 20" fill="none" stroke="var(--gold)" stroke-width="1.8"><path d="M10 18.5s-6-6.2-6-10.5a6 6 0 0 1 12 0c0 4.3-6 10.5-6 10.5z"/><circle cx="10" cy="8" r="2.2"/></svg>
      <span>48 Linden Grove, Suite 210<br>Maple Falls, GA 30412</span>
    </li>
    <li class="gap">
      <svg viewBox="0 0 20 20" fill="var(--gold)"><path d="M5 2.5l3 3.2-1.6 2.2c1 2 2.6 3.6 4.6 4.6l2.2-1.6 3.2 3-1.8 2.6C9.6 16.8 3.2 10.4 2.5 5.4z"/><path d="M12 3a5 5 0 0 1 5 5" fill="none" stroke="var(--gold)" stroke-width="1.5"/><path d="M12 6a2 2 0 0 1 2 2" fill="none" stroke="var(--gold)" stroke-width="1.5"/></svg>
      <span>000-123-456789</span>
    </li>
    <li>
      <svg viewBox="0 0 20 20" fill="var(--gold)"><path d="M2 5h16v10H2z"/><path d="M2 5l8 6 8-6" fill="none" stroke="var(--card-bg)" stroke-width="1.4"/></svg>
      <span>info@yourwebsitename.com</span>
    </li>
    <li>
      <svg viewBox="0 0 20 20" fill="none" stroke="var(--gold)" stroke-width="1.5"><circle cx="10" cy="10" r="8"/><ellipse cx="10" cy="10" rx="3.5" ry="8"/><path d="M2 10h16M3.5 6h13M3.5 14h13"/></svg>
      <span>www.yourwebsitename.com</span>
    </li>
  </ul>
</section>

<section class="card card--back">
  <div class="line-art" role="img" aria-label="Flowing bronze line-art drawing of a bird with open hands"></div>

  <div class="brand">
    <span class="brand__dot"></span>
    <span class="brand__name">STILLWATER REIKI</span>
  </div>
</section>

</body>
</html>
```